I need a direct mail postcard made up for my marketing campaign

I am starting a marketing campaign and need a design for a post card. I own an iron door company and need to have before and after images on the post card to showcase what our work looks like. I have provided pictures to use below.

The design needs to be two sided. The logo should be on the front.

The tag line for this campaign is: Design the smile your home deserves.

Words to also use: Distinctive style, Work of Art, One-of-a-Kind, Elegant, Modern, Innovative, Unique

My information for the card
Name: Dean Halvorsen
Phone number: (555)-318-2764
Email: Dean@forgelineentryways.example

The US postal system is very picky as to what can be sent in the mail. The only requirement they have is for the address. There needs to be a 2inch (50.8mm) by 4inch (101.6mm) blank space on the bottom right hand corner on the back of the card.

Target Market(s)

Home owners

Industry/Entity Type

Home Improvement

Font styles to use
Serif
Decorative

Colors
0555a3
ffffff
ec1f27

Requirements
Must have
• My logo, My contact information, before and after pictures
• Provided 3D images
Nice to have
• Words that describe iron doors
• A contrast between contemporary and ornate doors.

```html
<!DOCTYPE html>
<html lang="en">
<head>
<meta charset="utf-8">
<title>Forgeline Entryways – Postcard</title>
<link rel="stylesheet" href="https://fonts.googleapis.com/css2?family=Dosis:wght@600;700&family=Playfair+Display:ital,wght@0,900;1,400&display=swap">
<style>
  :root{
    --brand-blue:#1456a6;
    --brand-blue-deep:#0f4a93;
    --brand-red:#ec1f27;
    --navy-mark:#1b3d78;
    --white:#ffffff;
    --paper-fade:#dfe2e6;
    --stage:#b3b3b3;
    --base-strip:#4b5866;
    --foot-strip:#6d8fc2;
  }
  *{box-sizing:border-box;margin:0;padding:0}
  html,body{width:1052px;height:1200px;overflow:hidden;background:var(--stage)}
  .stage{position:absolute;left:0;top:0;width:1314px;height:1500px;transform:scale(0.8);transform-origin:0 0}
  .card{position:absolute;left:160px;width:996px;height:640px;overflow:hidden;
    background:linear-gradient(180deg,var(--white) 55%,var(--paper-fade) 100%);
    box-shadow:4px 6px 8px rgba(0,0,0,.35);font-family:"Dosis",sans-serif}
  .card--front{top:93px}
  .card--back{top:766px}

  /* front */
  .front-band{position:absolute;left:0;top:0;width:100%;height:402px;background:var(--brand-blue);border-top:22px solid var(--brand-blue-deep)}
  .headline{position:absolute;right:406px;top:48px;white-space:nowrap;color:var(--white);
    font-family:"Playfair Display",serif;font-weight:900;font-size:80px;letter-spacing:-1px;line-height:1;
    transform:scaleX(0.78);transform-origin:right top}
  .tagline{position:absolute;right:406px;top:136px;white-space:nowrap;color:var(--white);
    font-family:"Playfair Display",serif;font-style:italic;font-size:38px;line-height:1}
  .rule{position:absolute;left:45px;width:540px;height:2px;background:linear-gradient(90deg,transparent,rgba(255,255,255,.9) 15%,rgba(255,255,255,.9) 85%,transparent)}
  .rule--top{top:209px}.rule--bottom{top:365px}
  .traits{position:absolute;left:30px;top:222px;width:570px;text-align:center;color:var(--white);font-weight:600;font-size:33px;line-height:43px}
  .traits span{white-space:nowrap;margin:0 4px}
  .traits span::before{content:"";display:inline-block;border-left:11px solid var(--navy-mark);border-top:9px solid transparent;border-bottom:9px solid transparent;margin-right:5px;vertical-align:2px}

  .compare{position:absolute;border:3px solid var(--white);border-radius:16px;overflow:hidden;display:flex}
  .compare--front{left:618px;top:40px;width:346px;height:324px}
  .compare--back{left:302px;top:341px;width:243px;height:244px;border-color:var(--brand-blue);border-width:2px;border-radius:12px}
  .photo{height:100%}
  .label{position:absolute;bottom:0;background:var(--brand-red);color:var(--white);font-weight:700}
  .compare--front .label{font-size:23px;padding:4px 18px 2px}
  .compare--back .label{font-size:17px;padding:3px 12px 1px}
  .label--before{left:0;border-radius:0 12px 0 0}
  .label--after{right:0;border-radius:12px 0 0 0}

  .headshot{position:absolute;left:25px;top:377px;width:215px;height:235px;border:3px solid #3e4a57;border-radius:10px;
    background:linear-gradient(160deg,#c9d0d8 0%,#8c97a3 45%,#2b303a 100%)}
  .agent-name{position:absolute;left:265px;top:437px;color:var(--brand-blue);font-weight:700;font-size:56px;line-height:1;white-space:nowrap}
  .agent-phone{position:absolute;left:265px;top:500px;color:var(--brand-blue);font-weight:700;font-size:40px;line-height:1;white-space:nowrap}
  .agent-email{position:absolute;left:265px;top:552px;color:var(--brand-blue);font-weight:600;font-size:23px;line-height:1;white-space:nowrap}
  .door-render{position:absolute;top:416px;height:188px;border:2px solid var(--brand-blue)}
  .door-render--ornate{left:687px;width:141px;background:linear-gradient(135deg,#6b3a1e,#4a2511)}
  .door-render--modern{left:840px;width:115px;background:linear-gradient(90deg,#e9e9e9 0 22%,#5a2c14 22% 78%,#e9e9e9 78%)}
  .base-strip{position:absolute;left:0;bottom:0;width:100%;height:16px;background:var(--base-strip)}

  /* back */
  .back-band{position:absolute;left:0;top:0;width:100%;height:131px;background:var(--brand-blue);border-top:24px solid var(--brand-blue-deep)}
  .back-phone{position:absolute;left:48px;top:42px;color:var(--white);font-weight:700;font-size:72px;line-height:1;white-space:nowrap}
  .stamp-box{position:absolute;left:823px;top:62px;width:117px;height:116px;background:var(--white);border:2px solid #111}
  .trait-list{position:absolute;left:48px;top:168px;list-style:none;color:var(--brand-blue);font-weight:700;font-size:44px;line-height:56px}
  .trait-list li{white-space:nowrap}
  .trait-list li::before{content:"";display:inline-block;width:22px;height:22px;border-radius:50%;background:var(--brand-blue);margin-right:18px;vertical-align:4px}
  .brand-name{position:absolute;left:370px;top:215px;width:170px;text-align:center;color:var(--brand-blue);font-weight:700;font-size:26px;line-height:30px}
  .foot-strip{position:absolute;left:0;bottom:0;width:100%;height:21px;background:var(--foot-strip)}
</style>
</head>
<body>
<div class="stage">

  <section class="card card--front">
    <div class="front-band"></div>
    <h1 class="headline">Design the Smile</h1>
    <p class="tagline">your home deserves.</p>
    <div class="rule rule--top"></div>
    <p class="traits">
      <span>Distinctive style</span><span>Work of Art</span><br>
      <span>One-of-a-Kind</span><span>Elegant</span><span>Modern</span><br>
      <span>Innovative</span><span>Unique</span>
    </p>
    <div class="rule rule--bottom"></div>

    <div class="compare compare--front">
      <div class="photo" style="width:129px;background:linear-gradient(180deg,#8a4a2c,#5c2c17)" role="img" aria-label="Worn wooden double entry doors before replacement"></div>
      <div class="photo" style="width:3px;background:var(--white)"></div>
      <div class="photo" style="flex:1;background:linear-gradient(180deg,#3a3c40,#1c1d20 60%,#2a2620)" role="img" aria-label="Arched black wrought iron double doors with glass after installation"></div>
      <span class="label label--before">Before</span>
      <span class="label label--after">After</span>
    </div>

    <div class="headshot" role="img" aria-label="Portrait of Dean Halvorsen"></div>
    <h2 class="agent-name">Dean Halvorsen</h2>
    <p class="agent-phone">Ph: (555)-318-2764</p>
    <p class="agent-email">E: Dean@forgelineentryways.example</p>
    <div class="door-render door-render--ornate" role="img" aria-label="3D render of ornate arched iron double door"></div>
    <div class="door-render door-render--modern" role="img" aria-label="3D render of contemporary iron door with sidelights"></div>
    <div class="base-strip"></div>
  </section>

  <section class="card card--back">
    <div class="back-band"></div>
    <p class="back-phone">Ph: (555)-318-2764</p>
    <div class="stamp-box"></div>
    <ul class="trait-list">
      <li>Distinctive style</li>
      <li>Work of Art</li>
      <li>One-of-a-Kind</li>
      <li>Elegant</li>
      <li>Modern</li>
      <li>Innovative</li>
      <li>Unique</li>
    </ul>
    <p class="brand-name">Forgeline Entryways</p>

    <div class="compare compare--back">
      <div class="photo" style="width:100px;background:linear-gradient(180deg,#6b5a3c 0 12%,#f1f0ec 12%)" role="img" aria-label="Plain white double doors before replacement"></div>
      <div class="photo" style="flex:1;background:linear-gradient(180deg,#e9e4da 0 8%,#3b3a44 8%,#2a2a33)" role="img" aria-label="Arched iron double doors with holiday wreaths after installation"></div>
      <span class="label label--before">Before</span>
      <span class="label label--after">After</span>
    </div>
    <div class="foot-strip"></div>
  </section>

</div>
</body>
</html>
```